Stationary design and implementation for Swedish IT company

Hi,

I'm looking for a design and statiionary for my company (www.lumenfarro.example).

LumenFarro is an innovative company with four core values:
- Entrepreneurial; we take risks and the responsibility to create value
- Awarding; we work with fun and have added value to our relationships
- Innovation; we're creative and introduce new solutions
- Respect; we work with respect for our environment based on values instead of red tape

The required stationary should include:
- Powerpoint template
- Word templates
- Business card design
- e-mail signature

Please visit our site for more details.
Updates

Hi - please read (PRIORITY!),

You have been involved in one my projects. 

As it seems there is something seriously wrong with the participation payments at ArtHively. 

I have send invites with participation payments to reward designers for there work. It has been reported that these invitations resulted in expired messages, and payments have NOT been made. The money is withdrawn from my account and NOT paid to designers. This is a real shame when people do not get rewarded for the work done and the money is gone.

When you got an invitation with participation payment could you please let me know if the payment has actually been made? You can contact me at kmelvane@lumenfarro.example.

I'm trying to get this clarified with ArtHively.

Grt, Kees

Target Market(s)

Our market is IT and professional service in Sweden and other Nordics countries (Danmark, Norway, Finland).

Industry/Entity Type

Environment

Requirements
Must have
• Project delivery should include:
- Powerpoint template with title and content pages
- Standard letter (Word template)
- Standard invoice (Word template)
- Business card
- e-mail signature
Should not have
• Please await a logo to be attached (almost done).

```html
<!DOCTYPE html>
<html lang="en">
<head>
<meta charset="utf-8">
<title>LumenFarro Business Cards</title>
<link rel="stylesheet" href="https://fonts.googleapis.com/css2?family=Fira+Sans:wght@400;500;600&display=swap">
<style>
  :root {
    --board: #1d2d5c;
    --navy: #1e2f6a;
    --brand-blue: #2e55ad;
    --ink: #333333;
    --paper: #ffffff;
    --stone: #7c7d80;
    --shadow: rgba(0, 0, 0, 0.45);
  }
  * { box-sizing: border-box; margin: 0; padding: 0; }
  html, body {
    width: 1200px; height: 900px; overflow: hidden;
    background: var(--board);
    font-family: "Fira Sans", sans-serif;
  }
  .board { position: relative; width: 1200px; height: 900px; }

  .card {
    position: absolute;
    width: 510px; height: 294px;
    box-shadow: 3px 4px 8px var(--shadow);
    overflow: hidden;
  }
  .card--front-light { left: 64px; top: 90px; background: var(--paper); color: var(--ink); }
  .card--front-dark { left: 64px; top: 514px; background: var(--stone); color: var(--paper); }
  .card--back { left: 620px; top: 310px; background: var(--paper); }

  .tagline {
    position: absolute; right: 16px; top: 13px;
    font-size: 16px; font-weight: 400;
  }
  .person-name {
    position: absolute; left: 97px; top: 48px;
    font-size: 53px; font-weight: 600; letter-spacing: -0.5px;
    white-space: nowrap;
  }
  .card--front-light .person-name { color: var(--navy); }

  .contact-list { list-style: none; position: absolute; left: 16px; top: 136px; }
  .contact-item {
    display: flex; align-items: center;
    height: 29px; font-size: 15.5px; font-weight: 500;
    white-space: nowrap;
  }
  .contact-icon { width: 28px; height: 24px; margin-right: 22px; flex: none; }
  .card--front-light .contact-icon { color: var(--brand-blue); }
  .card--front-dark .contact-icon { color: var(--paper); }

  .web-box {
    position: absolute; right: 0; top: 226px;
    width: 182px; height: 32px;
    background: var(--brand-blue); color: var(--paper);
    font-size: 14px; font-weight: 600;
    display: flex; align-items: center; justify-content: center;
    white-space: nowrap;
  }
  .address-band {
    position: absolute; left: 0; bottom: 0;
    width: 100%; height: 34px;
    background: var(--navy); color: var(--paper);
    font-size: 15px; font-weight: 500;
    display: flex; align-items: center; padding-left: 16px;
    white-space: nowrap;
  }

  .brand-lockup { position: absolute; left: 18px; top: 100px; display: flex; align-items: center; height: 80px; }
  .brand-dot {
    width: 80px; height: 80px; border-radius: 50%;
    background: var(--brand-blue); margin-right: 24px; flex: none;
  }
  .brand-name {
    font-size: 66px; font-weight: 500; color: var(--navy);
    letter-spacing: -1px; line-height: 1; white-space: nowrap;
  }
  .brand-tagline {
    position: absolute; right: 17px; top: 174px;
    font-size: 21px; font-weight: 500; color: var(--navy);
    white-space: nowrap;
  }
</style>
</head>
<body>
<main class="board">

  <section class="card card--front-light">
    <p class="tagline">Bright ideas, real value</p>
    <h1 class="person-name">Kees Marveld</h1>
    <ul class="contact-list">
      <li class="contact-item">
        <svg class="contact-icon" viewBox="0 0 28 24"><rect x="2" y="4" width="24" height="16" fill="currentColor"/><path d="M2 4 L14 14 L26 4" fill="none" stroke="#fff" stroke-width="2"/></svg>
        kmelvane@lumenfarro.example
      </li>
      <li class="contact-item">
        <svg class="contact-icon" viewBox="0 0 28 24"><g transform="rotate(-35 14 12)"><rect x="9" y="1" width="11" height="22" rx="2" fill="none" stroke="currentColor" stroke-width="2.2"/><circle cx="14.5" cy="19" r="1.3" fill="currentColor"/></g></svg>
        +46 70 555 0142
      </li>
      <li class="contact-item">
        <svg class="contact-icon" viewBox="0 0 28 24"><path d="M6 3 L10 3 L12 8 L9.5 10 C11 13.5 13.5 16 17 17.5 L19 15 L24 17 L24 21 C14 22 4 12 6 3 Z" fill="currentColor"/></svg>
        +46 10 555 0178
      </li>
      <li class="contact-item">
        <svg class="contact-icon" viewBox="0 0 28 24"><circle cx="14" cy="12" r="9" fill="currentColor"/></svg>
        @lumenfarro
      </li>
    </ul>
    <div class="web-box">www.lumenfarro.example</div>
    <footer class="address-band">LumenFarro Ventures AB - Lindvägen 12, 131 40 Nacka, Sweden</footer>
  </section>

  <section class="card card--back">
    <div class="brand-lockup">
      <span class="brand-dot"></span>
      <span class="brand-name">LumenFarro</span>
    </div>
    <p class="brand-tagline">Bright ideas, real value</p>
  </section>

  <section class="card card--front-dark">
    <p class="tagline">Bright ideas, real value</p>
    <h1 class="person-name">Kees Marveld</h1>
    <ul class="contact-list">
      <li class="contact-item">
        <svg class="contact-icon" viewBox="0 0 28 24"><rect x="2" y="4" width="24" height="16" fill="currentColor"/><path d="M2 4 L14 14 L26 4" fill="none" stroke="#7c7d80" stroke-width="2"/></svg>
        kmelvane@lumenfarro.example
      </li>
      <li class="contact-item">
        <svg class="contact-icon" viewBox="0 0 28 24"><g transform="rotate(-35 14 12)"><rect x="9" y="1" width="11" height="22" rx="2" fill="none" stroke="currentColor" stroke-width="2.2"/><circle cx="14.5" cy="19" r="1.3" fill="currentColor"/></g></svg>
        +46 70 555 0142
      </li>
      <li class="contact-item">
        <svg class="contact-icon" viewBox="0 0 28 24"><path d="M6 3 L10 3 L12 8 L9.5 10 C11 13.5 13.5 16 17 17.5 L19 15 L24 17 L24 21 C14 22 4 12 6 3 Z" fill="currentColor"/></svg>
        +46 10 555 0178
      </li>
      <li class="contact-item">
        <svg class="contact-icon" viewBox="0 0 28 24"><circle cx="14" cy="12" r="9" fill="currentColor"/></svg>
        @lumenfarro
      </li>
    </ul>
    <div class="web-box">www.lumenfarro.example</div>
    <footer class="address-band">LumenFarro Ventures AB - Lindvägen 12, 131 40 Nacka, Sweden</footer>
  </section>

</main>
</body>
</html>
```